Tarn Valley Performances

We would like a design to fit on a retractable cloth banner
size - 590mm x 1490mm

We want to promote our live music business at expos (weddings, corporate events and private parties are our bread and butter)

Our focus is Jazz and Classical music - although we offer rock/pop/contemporary also

We need our contacts on there also - i'm happy to go with what you suggest

email: tarn_valley@quillnet.com
mob: 0498 215 764
web: www.tarnvalley.com.au

Target Market(s)

Live Music for:
Corporate Events
Weddings
Private Parties

Industry/Entity Type

Events

Font styles to use
Serif
Sans Serif

Colors
f78f20

Requirements
Must have
• Would love you to pic appropriate shots from our website at http://www.tarnvalley.com.au

if you need better resolution sent through please let me know and i will upload

```html
<!DOCTYPE html>
<html lang="en">
<head>
<meta charset="utf-8">
<title>Tarn Valley Performances – Expo Banner</title>
<link rel="stylesheet" href="https://fonts.googleapis.com/css2?family=Quicksand:wght@500&family=Roboto+Slab:wght@300;400;700&family=Lobster+Two:wght@700&display=swap">
<style>
  :root {
    --stage: #d8d5d2;
    --charcoal: #2b2626;
    --charcoal-deep: #1e1a1a;
    --charcoal-soft: #332d2d;
    --orange: #f78f20;
    --orange-deep: #e5701a;
    --white: #ffffff;
    --ink: #231f1f;
  }
  * { margin: 0; padding: 0; box-sizing: border-box; }
  html, body { width: 1200px; height: 675px; overflow: hidden; background: var(--stage); }
  .canvas { position: relative; width: 1200px; height: 675px; overflow: hidden; background: var(--stage); }
  .defs { position: absolute; width: 0; height: 0; overflow: hidden; }
  .view { position: absolute; display: block; }
  .view--top { left: 33px; top: 29px; width: 396px; height: 646px; }
  .view--lower { left: 486px; top: 0; width: 396px; height: 590px; }
  .view--full { left: 930px; top: 29px; width: 242px; height: 611px; }

  .brand-name { font-family: "Quicksand", sans-serif; font-weight: 500; fill: var(--white); }
  .tagline { font-family: "Roboto Slab", serif; font-weight: 400; fill: var(--ink); font-size: 38px; }
  .genre-script { font-family: "Lobster Two", cursive; font-weight: 700; fill: var(--white); font-size: 58px; }
  .genre-caps { font-family: "Roboto Slab", serif; font-weight: 400; fill: var(--white); font-size: 46px; font-variant: small-caps; letter-spacing: 1px; }
  .contact { font-family: "Roboto Slab", serif; font-weight: 300; fill: var(--white); font-size: 31px; }
  .cta { font-family: "Roboto Slab", serif; font-weight: 400; fill: var(--white); font-size: 32px; }
  .event-label { font-family: "Roboto Slab", serif; font-weight: 700; fill: var(--white); font-size: 33px; }
</style>
</head>
<body>
<div class="canvas">

  <svg class="defs" aria-hidden="true">
    <defs>
      <linearGradient id="tone-violin" x1="0" y1="0" x2="1" y2="1">
        <stop offset="0" stop-color="#6b4530"/><stop offset="1" stop-color="#2a1d18"/>
      </linearGradient>
      <linearGradient id="tone-ensemble" x1="0" y1="0" x2="1" y2="1">
        <stop offset="0" stop-color="#cfcfcf"/><stop offset="1" stop-color="#7d7d7d"/>
      </linearGradient>
      <linearGradient id="tone-piano" x1="0" y1="0" x2="1" y2="1">
        <stop offset="0" stop-color="#4a4a4c"/><stop offset="1" stop-color="#1f1f21"/>
      </linearGradient>
      <linearGradient id="tone-ballroom" x1="0" y1="0" x2="1" y2="1">
        <stop offset="0" stop-color="#b5b5b5"/><stop offset="1" stop-color="#4f4f4f"/>
      </linearGradient>
      <linearGradient id="tone-microphone" x1="0" y1="0" x2="1" y2="1">
        <stop offset="0" stop-color="#a07a55"/><stop offset="1" stop-color="#4a3322"/>
      </linearGradient>
      <linearGradient id="tone-cellist" x1="0" y1="0" x2="1" y2="1">
        <stop offset="0" stop-color="#8a6a48"/><stop offset="1" stop-color="#2e2119"/>
      </linearGradient>

      <symbol id="banner" viewBox="0 0 590 1490">
        <!-- brand header -->
        <rect class="brand-panel" x="0" y="0" width="590" height="1490" fill="var(--charcoal)"/>
        <circle class="brand-dot" cx="62" cy="160" r="30" fill="var(--orange)"/>
        <text class="brand-name" x="112" y="150" font-size="60">Tarn Valley</text>
        <text class="brand-name" x="112" y="218" font-size="52">Performances</text>

        <!-- tagline band -->
        <rect class="tagline-band" x="0" y="256" width="590" height="80" fill="var(--white)"/>
        <text class="tagline" x="22" y="310" textLength="540" lengthAdjust="spacingAndGlyphs">Book Distinctive Live Music</text>

        <!-- genre band -->
        <polygon class="genre-band" points="0,336 590,336 590,428 0,517" fill="var(--orange)"/>
        <text class="genre-script" x="16" y="418" transform="rotate(-8.6 16 418)">Jazz</text>
        <text class="genre-caps" x="140" y="428" transform="rotate(-8.6 140 428)">Classical</text>
        <text class="genre-script" x="398" y="400" transform="rotate(-8.6 398 400)">Dance</text>

        <!-- contact strips -->
        <polygon class="strip strip--email" points="0,517 590,428 590,523 0,612" fill="var(--charcoal-soft)"/>
        <polygon class="strip strip--phone" points="0,612 590,523 590,618 0,707" fill="var(--charcoal)"/>
        <polygon class="strip strip--web" points="0,707 590,618 590,720 0,820" fill="var(--charcoal-soft)"/>
        <polygon class="strip-shadow" points="0,517 590,428 590,440 0,529" fill="var(--charcoal-deep)" opacity="0.7"/>
        <polygon class="strip-shadow" points="0,612 590,523 590,533 0,622" fill="var(--charcoal-deep)" opacity="0.7"/>
        <polygon class="strip-shadow" points="0,707 590,618 590,628 0,717" fill="var(--charcoal-deep)" opacity="0.7"/>

        <g class="contact-icon contact-icon--email">
          <circle cx="48" cy="568" r="26" fill="var(--orange-deep)"/>
          <rect x="34" y="558" width="28" height="20" rx="2" fill="var(--white)"/>
          <polyline points="34,559 48,570 62,559" fill="none" stroke="var(--orange-deep)" stroke-width="2.5"/>
        </g>
        <text class="contact" x="94" y="578" transform="rotate(-8.6 94 578)">tarn_valley@quillnet.com</text>

        <g class="contact-icon contact-icon--phone">
          <circle cx="52" cy="664" r="26" fill="var(--orange-deep)"/>
          <path d="M42 652 q-4 4 0 12 q6 10 14 14 q8 3 12 -1 l-6 -6 q-3 2 -6 0 q-5 -4 -8 -9 q-1 -3 1 -5 z" fill="var(--white)"/>
        </g>
        <text class="contact" x="102" y="672" transform="rotate(-8.6 102 672)">0498 215 764</text>

        <g class="contact-icon contact-icon--web" fill="none" stroke="var(--charcoal)" stroke-width="2.4">
          <circle cx="52" cy="758" r="26" fill="var(--orange-deep)" stroke="none"/>
          <circle cx="52" cy="758" r="15"/>
          <ellipse cx="52" cy="758" rx="6.5" ry="15"/>
          <line x1="37" y1="758" x2="67" y2="758"/>
          <line x1="40" y1="750" x2="64" y2="750"/>
          <line x1="40" y1="766" x2="64" y2="766"/>
        </g>
        <text class="contact" x="100" y="770" transform="rotate(-8.6 100 770)">www.tarnvalley.com.au</text>

        <!-- call to action wedge -->
        <polygon class="cta-wedge" points="230,810 590,712 590,794 287,794 287,810" fill="var(--orange)"/>
        <text class="cta" x="420" y="790" transform="rotate(-8.6 420 790)">Book Now</text>

        <!-- photo grid -->
        <rect x="0" y="807" width="287" height="209" fill="url(#tone-violin)" role="img" aria-label="Photo: violinist playing in an ensemble"/>
        <rect x="287" y="794" width="303" height="167" fill="url(#tone-ensemble)" role="img" aria-label="Photo: band with congas and double bass, black and white"/>
        <rect x="0" y="1016" width="287" height="216" fill="url(#tone-piano)" role="img" aria-label="Photo: close-up of piano keys"/>
        <rect x="287" y="961" width="303" height="271" fill="url(#tone-ballroom)" role="img" aria-label="Photo: ballroom with string lights, black and white"/>
        <rect x="0" y="1232" width="245" height="258" fill="url(#tone-microphone)" role="img" aria-label="Photo: vintage stage microphone"/>
        <rect x="245" y="1232" width="345" height="258" fill="url(#tone-cellist)" role="img" aria-label="Photo: cellist performing"/>

        <!-- event circles -->
        <circle class="event-circle" cx="170" cy="1206" r="114" fill="var(--orange)" opacity="0.88"/>
        <circle class="event-circle" cx="386" cy="1121" r="105" fill="var(--charcoal)" opacity="0.88"/>
        <circle class="event-circle" cx="356" cy="1291" r="115" fill="var(--orange)" opacity="0.85"/>
        <text class="event-label" x="94" y="1196">corporate</text>
        <text class="event-label" x="94" y="1226">events</text>
        <text class="event-label" x="318" y="1136">private</text>
        <text class="event-label" x="318" y="1166">parties</text>
        <text class="event-label" x="294" y="1284">Wedding</text>
        <text class="event-label" x="294" y="1314">Music</text>
      </symbol>
    </defs>
  </svg>

  <svg class="view view--top" viewBox="0 0 590 962" preserveAspectRatio="xMinYMin slice" aria-label="Banner top section">
    <use href="#banner" width="590" height="1490"/>
  </svg>

  <svg class="view view--lower" viewBox="0 611 590 879" preserveAspectRatio="xMinYMin slice" aria-label="Banner lower section">
    <use href="#banner" width="590" height="1490"/>
  </svg>

  <svg class="view view--full" viewBox="0 0 590 1490" preserveAspectRatio="xMinYMin meet" aria-label="Full banner">
    <use href="#banner" width="590" height="1490"/>
  </svg>

</div>
</body>
</html>
```